Book Cover Design | Science & Nature

We are looking for a cover design for our new educational book titled "Moths Beyond the Hedge".
The full title on the cover can either only be "Moths Beyond the Hedge" or "Garden Moths Beyond the Hedge - a pocket handbook". Up to you what looks good. If the latter, the words "Moths Beyond the Hedge" should be written in larger letters.
The book has a lot information about spiders in general and provides a convenient and understandable identification guide about spiders in California.
The target audience are normal, non-scientist readers who would like to get a simple guide that helps them identify common spiders they will find inside their homes and gardens.
The book is written in an understandable, non-scientific language and contains numerous illustrations and identification sheets of all common spiders.
We are fairly open to suggestions about the design. It should not be too plain as it is not a classic boring science book, but aimed at the average reader. Readers are both male and female, aged 30 and above.
If you know nothing about spiders but would like to know what the spiders in your backyard are, which ones are dangerous and if you want to learn more about spiders, this should be the book you will want to buy!
The author is Dale Prowse. In addition to the author, the book cover should show "Brindlewing.com" - The author can be at the bottom and the website on the top or vice versa.
The cover size is 6" x 9" (15.24 x 22.86 cm). The book has around 150 pages. The back of the book should have a placeholder for the barcode as well as some text. It should also have a quick overview of the main benefits of the book: Easily understandable for non-scientist readers, helpful illustrations, tips on how to deal with spiders in the house and with spider bites. We will obviously add the text later.
I've attached a few of the illustrations as I think they could be used to already give the reader a feeling what they will get with the book. If you think a stock photo will work better than the illustrations, that is fine too.

Target Market(s)

Average readers in the United States wanting to learn more about spiders

Industry/Entity Type

Science, Nature, Spiders, Animals, Education

Requirements
Must have
• When the artwork is generated, the files we would like to receive are: The original working file PSD (Photoshop Document - so any text and images can be edited) All the working elements including: illustrations, photos, graphics and fonts A high resolution (300 dpi), 8.5 x 11 (o- Once r larger) file A JPG file in the exact size specifications and color required by our publisher A JPG file in the exact size for online POD or ebook (Pagelume requires 900x600 ) A JPG black and white (gray scale) variation
Nice to have
• A text (overlay?) could point out some of the advantages of this book: Illustrations and identification guides for all common California spiders, tips on how to get rid of spiders from inside the house, tips on how to deal with arachnophobia, etc. This is optional. Maybe something like "An easy to understand identification guide with plenty of tips and illustrations".
Should not have
• Very dark colors or very feminine colors or shapes.

```html
<!DOCTYPE html>
<html lang="en">
<head>
<meta charset="utf-8">
<title>Moths Beyond the Hedge — Book Cover</title>
<link rel="stylesheet" href="https://fonts.googleapis.com/css2?family=Encode+Sans+Condensed:wght@300;400;600&display=swap">
<style>
  :root {
    --page-bg: #ececea;
    --cover-bg: #fbfbfb;
    --title-red: #e01b22;
    --ink: #1c1c1c;
    --rule: #6f6f6f;
    --photo-light: #f4f2ef;
    --photo-mid: #cdbba4;
    --photo-deep: #8a7560;
  }
  * { margin: 0; padding: 0; box-sizing: border-box; }
  html, body {
    width: 1200px; height: 800px; overflow: hidden;
    background: var(--page-bg);
    font-family: "Encode Sans Condensed", "Arial Narrow", sans-serif;
  }
  .canvas { position: relative; width: 1200px; height: 800px; }
  .cover {
    position: absolute; left: 340px; top: 18px;
    width: 520px; height: 764px;
    background: var(--cover-bg);
    box-shadow: 0 2px 10px rgba(0,0,0,0.12);
    overflow: hidden;
  }
  .cover-photo {
    position: absolute; left: 0; top: 0; width: 520px; height: 340px;
    background:
      radial-gradient(ellipse 45% 30% at 40% 52%, rgba(60,50,30,0.35), transparent 70%),
      linear-gradient(160deg, var(--photo-light) 0%, var(--photo-light) 45%, var(--photo-mid) 75%, var(--photo-deep) 100%);
    -webkit-mask-image: linear-gradient(to bottom, #000 75%, transparent 100%);
    mask-image: linear-gradient(to bottom, #000 75%, transparent 100%);
  }
  .title { position: absolute; left: 0; width: 100%; text-align: center; }
  .title-main {
    top: 338px;
    font-weight: 300; font-size: 140px; line-height: 1;
    color: var(--title-red); letter-spacing: 1px;
  }
  .title-sub {
    top: 458px;
    font-weight: 300; font-size: 64px; line-height: 1;
    color: var(--ink); letter-spacing: 1px;
  }
  .title-sub .lead {
    font-size: 26px; vertical-align: 26px; margin-right: 8px; letter-spacing: 0.5px;
  }
  .title-rule {
    position: absolute; left: 113px; top: 546px;
    width: 298px; height: 1px; background: var(--rule);
  }
  .subtitle {
    position: absolute; left: 0; width: 100%; top: 555px; text-align: center;
    font-weight: 300; font-size: 32px; line-height: 1; color: var(--ink);
  }
  .author {
    position: absolute; left: 0; width: 100%; top: 660px; text-align: center;
    font-weight: 300; font-size: 44px; line-height: 1;
    color: var(--title-red); letter-spacing: 9px;
  }
  .website {
    position: absolute; left: 0; width: 100%; top: 708px; text-align: center;
    font-weight: 400; font-size: 26px; line-height: 1; color: var(--ink);
  }
</style>
</head>
<body>
  <div class="canvas">
    <div class="cover">
      <div class="cover-photo" role="img" aria-label="Photograph of a moth resting on a bare twig against a white background"></div>
      <h1>
        <span class="title title-main">MOTHS</span>
        <span class="title title-sub"><span class="lead">BEYOND</span>THE HEDGE</span>
      </h1>
      <div class="title-rule"></div>
      <p class="subtitle">A POCKET HANDBOOK</p>
      <p class="author">DALE PROWSE</p>
      <p class="website">Brindlewing.com</p>
    </div>
  </div>
</body>
</html>
```